Poster Design Project- kids dancing/sport

I need a poster design for a childrens dance and sport program!!
I have attached a brochure and logo designs. From the brochure please include information from sections titled "twirl'n'hop" and "themes". Also please put on the phone number and email address (found on the brochure). Emphasis on FUN!! Make poster colourful, very kid friendly and eye catching.
Some other things i would like on the poster are:
"Does your child love to dance, sing and play sport?? Why not enrol them in our fun-filled program?"
"From only $10.00 per class"
"Sign up for your FREE trial class today"
"A fun introduction to the joy of Dance, Sport and Music for 2-6yr olds. Held in your childcare centre!!"
Hi!!
I would like to stress its TRIAL class not TRAIL class. Please feel free to play around with the information, it doesnt need to be in one blurb. Also i have updated the brief. I would like "Does you child love to dance, sing or play sport? Why not enrol in our fun filled program?" or something to that effect!!
Thanks!!!!
2-6yr olds and their parents
Childcare

```html
<!DOCTYPE html>
<html lang="en">
<head>
<meta charset="utf-8">
<title>Twirl 'n' Hop – Childrens Dance &amp; Sport Program</title>
<link rel="stylesheet" href="https://fonts.googleapis.com/css2?family=Ribeye&family=Delius&display=swap">
<style>
  :root {
    --violet: #5a22d6;
    --navy: #2b2aa8;
    --magenta: #e2239a;
    --card-white: #ffffff;
    --sky: #cde9fb;
    --pink-glow: #fbd3ef;
    --sun-glow: #fff1b8;
    --ray-red: #f0252f;
    --ray-orange: #ff8a1c;
    --ray-yellow: #ffe21a;
    --ray-green: #39c93a;
    --ray-cyan: #1fc3ef;
    --ray-blue: #2f4fe0;
    --ray-purple: #9a2fe0;
    --ray-pink: #ff3fb3;
    --dancer-blue: #5b9be8;
    --dancer-pale: #e3effc;
  }
  * { box-sizing: border-box; margin: 0; padding: 0; }
  html, body { width: 1200px; height: 845px; overflow: hidden; background: #fff; }
  .poster {
    position: relative;
    width: 1200px;
    height: 845px;
    overflow: hidden;
    font-family: "Delius", "Comic Sans MS", cursive;
  }
  .rainbow-backdrop {
    position: absolute; inset: 0;
    background:
      radial-gradient(circle at 50% 50%, rgba(255,255,255,0.35) 0%, rgba(255,255,255,0) 60%),
      conic-gradient(from 0deg at 50% 50%,
        var(--ray-red), var(--ray-orange), var(--ray-yellow), var(--ray-green),
        var(--ray-cyan), var(--ray-blue), var(--ray-purple), var(--ray-pink),
        var(--ray-red), var(--ray-orange), var(--ray-yellow), var(--ray-green),
        var(--ray-cyan), var(--ray-blue), var(--ray-purple), var(--ray-pink), var(--ray-red));
  }
  .card-frame { position: absolute; inset: 0; }
  .logo-burst {
    position: absolute;
    left: 250px; top: 70px;
    width: 700px; height: 200px;
    border-radius: 50%;
    background: radial-gradient(ellipse at 50% 50%,
      rgba(255,241,184,0.95) 0%, rgba(251,211,239,0.85) 40%,
      rgba(205,233,251,0.6) 65%, rgba(255,255,255,0) 80%);
  }
  .logo {
    position: absolute;
    left: 0; width: 1200px;
    top: 102px;
    text-align: center;
    font-family: "Ribeye", "Georgia", serif;
    font-weight: 400;
    font-size: 74px;
    line-height: 68px;
    color: var(--violet);
    letter-spacing: 3px;
  }
  .kids-photo {
    position: absolute;
    left: 184px; top: 262px;
    width: 382px; height: 410px;
    border-radius: 36px;
    background: linear-gradient(160deg, var(--dancer-pale) 0%, #b8d6f7 40%, var(--dancer-blue) 100%);
  }
  .headline {
    position: absolute;
    left: 612px; top: 290px;
    font-family: "Ribeye", "Georgia", serif;
    font-weight: 400;
    line-height: 1.2;
  }
  .headline .line-one { display: block; font-size: 31px; color: var(--navy); }
  .headline .line-two { display: block; font-size: 33px; color: var(--magenta); padding-left: 36px; }
  .invite {
    position: absolute;
    left: 648px; top: 400px;
    font-size: 23px;
    line-height: 29px;
  }
  .invite .ask { color: var(--navy); }
  .invite .enrol { color: var(--magenta); }
  .details {
    position: absolute;
    left: 648px; top: 522px;
    font-size: 15px;
    line-height: 25px;
    color: var(--navy);
  }
  .details .price { font-size: 26px; color: var(--magenta); vertical-align: -2px; }
  .details .accent { color: var(--magenta); }
  .divider {
    position: absolute;
    left: 275px; top: 701px;
    width: 643px;
    border-top: 2px dotted var(--magenta);
  }
  .contact {
    position: absolute;
    left: 0; width: 1200px;
    top: 712px;
    text-align: center;
    font-family: "Ribeye", "Georgia", serif;
    font-size: 23px;
    color: var(--navy);
  }
  .contact .label { color: var(--magenta); text-decoration: underline; }
  .contact .email { color: var(--magenta); }
</style>
</head>
<body>
<main class="poster">
  <div class="rainbow-backdrop" role="img" aria-label="Bright rainbow sunburst of coloured rays"></div>

  <svg class="card-frame" width="1200" height="845" viewBox="0 0 1200 845" aria-hidden="true">
    <defs>
      <linearGradient id="card-fill" x1="0" y1="0" x2="0" y2="1">
        <stop offset="0" stop-color="var(--sky)"/>
        <stop offset="0.2" stop-color="var(--pink-glow)"/>
        <stop offset="0.38" stop-color="#eef6fd"/>
        <stop offset="0.6" stop-color="var(--card-white)"/>
        <stop offset="1" stop-color="var(--card-white)"/>
      </linearGradient>
    </defs>
    <path d="M 140 52 H 1060 A 70 70 0 0 0 1130 112 Q 1100 200 1130 300 Q 1170 380 1160 420 Q 1170 470 1130 540 Q 1100 640 1130 732 A 70 70 0 0 0 1060 796 H 140 A 70 70 0 0 0 70 732 Q 100 640 70 540 Q 30 470 40 420 Q 30 380 70 300 Q 100 200 70 112 A 70 70 0 0 0 140 52 Z"
          fill="url(#card-fill)" stroke="#ffffff" stroke-width="8"/>
  </svg>

  <div class="logo-burst" role="img" aria-label="Colourful starburst with stars and music notes"></div>
  <h1 class="logo">TWIRL 'N'<br>HOP</h1>

  <div class="kids-photo" role="img" aria-label="Photo of three young dancers in blue and white costumes"></div>

  <h2 class="headline">
    <span class="line-one">Childrens dance</span>
    <span class="line-two">&amp; Sport program!!</span>
  </h2>

  <p class="invite">
    <span class="ask">Does your child love to<br>dance, sing &amp; play sport??</span><br>
    <span class="enrol">Why not enrol them in<br>our fun-filled program?"</span>
  </p>

  <p class="details">
    "From only <span class="price">$10.00</span> per class"<br>
    "Sign up for your FREE trial class today"<br>
    "A fun introduction to the joy of Dance,<br>
    <span class="accent">Sport and Music for 2-6yr olds,</span><br>
    Held in your childcare centre!!"
  </p>

  <div class="divider"></div>

  <p class="contact">
    <span class="label">Ph:</span> 0400 218 765 &bull; <span class="label">E:</span> <span class="email">twirlnhop@kidmail.com</span>
  </p>
</main>
</body>
</html>
```